Animated banner ad design (gif)

We are LeaseVarn (www.LeaseVarn.example)
a tech company in the commercial real estate industry. Our audience / customers are commercial real estate brokers, appraisers and researchers. They go to LeaseVarn to trade information about commercial leases. You can learn more about LeaseVarn by reading this:

http://leasevarn.example/gateway/about

and watching this video:

http://clipmoor.example/71920485

The goal of the ad is to direct commercial real estate professional from the San Francisco Bay area to our sign up page, where they can sign up for a membership

The ad details:

1) 600 pixels wie x 90 pixels tall
2) Should be animated. Can have multiple panels
3) Preferred file-type is .gif

Ad text:

Immediate access to thousands of San Francisco and Bay commercial lease comps
Free * Accurate * Comprehensive * Anonymous

Ad link:
http://leasevarn.example/account/signUp/index#crePro

The attached screenshot has some static ads that we've used before. This is just an example and by no means should guide your work.

Target Market(s)

Commercial Real Estate Professionals in The SF Bay Area

Industry/Entity Type

Real Estate

Requirements
Must have
• Animated ad

Link to LeaseVarn:

```html
<!DOCTYPE html>
<html lang="en">
<head>
<meta charset="utf-8">
<title>LeaseVarn – San Francisco &amp; Bay commercial lease comps</title>
<link rel="stylesheet" href="https://fonts.googleapis.com/css2?family=Arimo:wght@400;700&family=Great+Vibes&display=swap">
<style>
  :root {
    --sky-top: #3d4248;
    --sky-mid: #22262b;
    --sky-low: #4a4f55;
    --ink-white: #ffffff;
    --city-blue: #2196d8;
    --bay-coral: #e8695b;
    --mark-blue: #2a8fd0;
  }
  html, body {
    margin: 0;
    padding: 0;
    width: 1200px;
    height: 180px;
    overflow: hidden;
    background: #000;
  }
  .banner {
    display: block;
    position: relative;
    width: 1200px;
    height: 180px;
    overflow: hidden;
    text-decoration: none;
    font-family: "Arimo", Arial, sans-serif;
  }
  .skyline-backdrop {
    position: absolute;
    inset: 0;
    background:
      linear-gradient(180deg, rgba(0,0,0,0.1) 0%, rgba(0,0,0,0) 40%, rgba(0,0,0,0.4) 100%),
      linear-gradient(90deg, #15181b 0%, var(--sky-mid) 15%, var(--sky-top) 40%, var(--sky-low) 62%, var(--sky-mid) 85%, #15181b 100%);
  }
  .brand-mark {
    position: absolute;
    left: 10px;
    top: 90px;
    width: 60px;
    height: 64px;
    background: var(--mark-blue);
  }
  .lead-in {
    position: absolute;
    right: 822px;
    top: 4px;
    margin: 0;
    color: var(--ink-white);
    font-size: 31px;
    line-height: 38px;
    text-align: right;
    font-weight: 400;
    white-space: nowrap;
  }
  .headline {
    position: absolute;
    inset: 0;
  }
  .headline .city { fill: var(--city-blue); font-family: "Arimo", Arial, sans-serif; }
  .headline .bay { fill: var(--bay-coral); font-family: "Arimo", Arial, sans-serif; }
  .headline .amp { fill: var(--ink-white); font-family: "Great Vibes", cursive; }
  .tail {
    position: absolute;
    right: 12px;
    top: 92px;
    margin: 0;
    color: var(--ink-white);
    font-size: 29px;
    line-height: 38px;
    text-align: right;
    white-space: nowrap;
  }
</style>
</head>
<body>
<a class="banner" href="http://leasevarn.example/account/signUp/index#crePro" aria-label="LeaseVarn: immediate access to thousands of San Francisco and Bay commercial lease comps">
  <div class="skyline-backdrop" role="img" aria-label="Dimmed black-and-white photo of the San Francisco city skyline"></div>
  <div class="brand-mark" aria-hidden="true"></div>
  <p class="lead-in">Immediate access<br>to thousands of</p>
  <svg class="headline" width="1200" height="180" viewBox="0 0 1200 180" aria-hidden="true">
    <text class="city" x="390" y="92" font-size="122" textLength="160" lengthAdjust="spacingAndGlyphs">SAN</text>
    <text class="city" x="88" y="172" font-size="112" textLength="462" lengthAdjust="spacingAndGlyphs">FRANSISCO</text>
    <text class="amp" x="576" y="146" font-size="150">&amp;</text>
    <text class="bay" x="700" y="136" font-size="176" textLength="300" lengthAdjust="spacingAndGlyphs">BAY</text>
  </svg>
  <p class="tail">commercial<br>lease comps</p>
</a>
</body>
</html>
```